Gardener needs an exciting new flyer design.

I'm a passionate gardener that requires a custom flyer design for a owner operator gardening business. Design will be for a DL flyer. I'm based on the Sunshine coast in Queensland Australia. My target audience is the residential market on the Sunshine coast. Business name is Marlowe Greens. My services are, lawn mowing, weeding, Eco Friendly fertilizing, green waste removal, Mulching, tree and shrub pruning, Full garden makeovers, hedging, pressure cleaning, privacy screening, Timber deck rejuvenation, Planting, Turf preparation and installation, and much more. Free no obligation quotes, reliable and friendly service, great rates. 12 years experience. Web www.marlowegreens.com.au - Phone 0418527064 - Email doug@marlowegreens.com.au I would like the design to portray a friendly and professional approach.

Target Market(s)

Residential

Industry/Entity Type

Gardener

Font styles to use
Serif

Colors
9ccb3b
abd037
3176b5

Requirements
Must have
• my services, my logo, my contact details,

```html
<!DOCTYPE html>
<html lang="en">
<head>
<meta charset="utf-8">
<title>Marlowe Greens – DL Flyer</title>
<link rel="stylesheet" href="https://fonts.googleapis.com/css2?family=Bebas+Neue&family=Merriweather:wght@400;700&display=swap">
<style>
  :root {
    --lime: #abd037;
    --lime-bright: #b6da3c;
    --charcoal: #2a2a2a;
    --charcoal-soft: #333333;
    --ink: #1c1c1c;
    --paper-text: #e6e6e6;
    --backdrop: #dedede;
    --leaf-dark: #2f4a1f;
    --leaf-mid: #4f7a2e;
  }
  html, body {
    margin: 0;
    width: 1200px;
    height: 900px;
    overflow: hidden;
    background: var(--backdrop);
  }
  .flyer {
    position: absolute;
    left: 395px;
    top: 20px;
    width: 410px;
    height: 860px;
    background: var(--charcoal);
    overflow: hidden;
    box-shadow: 0 6px 18px rgba(0,0,0,0.18);
  }
  .hero-photo {
    position: absolute;
    left: 0; top: 0;
    width: 410px; height: 395px;
    background:
      radial-gradient(ellipse at 70% 85%, rgba(255,255,255,0.55) 0 18%, transparent 45%),
      radial-gradient(ellipse at 15% 30%, #6f9a3f 0 20%, transparent 55%),
      linear-gradient(180deg, #8fb0c9 0%, #5d7f3a 30%, var(--leaf-mid) 60%, var(--leaf-dark) 100%);
  }
  .brand-panel {
    position: absolute;
    left: 78px; top: 0;
    width: 205px; height: 215px;
    background: var(--charcoal-soft);
    text-align: center;
    box-sizing: border-box;
    padding-top: 58px;
  }
  .brand-mark {
    width: 34px; height: 34px;
    margin: 0 auto 10px;
    border-radius: 50%;
    background: var(--lime);
  }
  .brand-name {
    font-family: 'Merriweather', serif;
    font-weight: 700;
    font-size: 19px;
    color: var(--lime);
    margin: 0 0 10px;
  }
  .selling-points {
    list-style: none;
    margin: 0; padding: 0;
    font-family: 'Bebas Neue', sans-serif;
    font-size: 16px;
    letter-spacing: 0.3px;
    color: var(--lime);
    line-height: 1.3;
  }
  .selling-points svg { vertical-align: -1px; margin-right: 4px; }
  .tagline-band {
    position: absolute;
    left: 0; top: 395px;
    width: 410px; height: 58px;
    background: var(--lime);
    display: flex; align-items: center; justify-content: center;
  }
  .tagline {
    font-family: 'Bebas Neue', sans-serif;
    font-size: 27px;
    color: var(--ink);
    margin: 0;
    letter-spacing: 0.2px;
  }
  .intro {
    position: absolute;
    left: 24px; top: 470px; width: 362px;
    margin: 0;
    font-family: 'Merriweather', serif;
    font-size: 11.5px;
    line-height: 1.45;
    color: var(--paper-text);
    text-align: center;
  }
  .services-title {
    position: absolute;
    left: 0; top: 540px; width: 410px;
    margin: 0;
    text-align: center;
    font-family: 'Bebas Neue', sans-serif;
    font-size: 30px;
    color: var(--lime);
    font-weight: 400;
  }
  .services {
    position: absolute;
    left: 24px; top: 580px; width: 370px;
    display: flex; justify-content: space-between;
  }
  .services ul {
    list-style: none; margin: 0; padding: 0;
    font-family: 'Merriweather', serif;
    font-size: 11px;
    line-height: 1.6;
    color: var(--paper-text);
  }
  .cta {
    position: absolute;
    left: 0; top: 718px; width: 410px;
    margin: 0;
    text-align: center;
    font-family: 'Bebas Neue', sans-serif;
    font-size: 50px;
    color: var(--lime-bright);
    font-weight: 400;
    line-height: 1;
  }
  .contact-band {
    position: absolute;
    left: 0; bottom: 0;
    width: 410px; height: 80px;
    background: var(--lime);
    font-family: 'Merriweather', serif;
    font-weight: 700;
    font-size: 12px;
    color: var(--ink);
    text-align: center;
    display: flex; flex-direction: column; justify-content: center;
    gap: 6px;
  }
  .contact-band p { margin: 0; }
  .divider { margin: 0 8px; font-weight: 400; }
</style>
</head>
<body>
  <article class="flyer">
    <div class="hero-photo" role="img" aria-label="Photograph of a lush residential garden with white daisies, shrubs and a house behind trees"></div>

    <header class="brand-panel">
      <div class="brand-mark"></div>
      <p class="brand-name">Marlowe Greens</p>
      <ul class="selling-points">
        <li><svg width="11" height="10" viewBox="0 0 11 10"><path d="M1 5l3 3 6-7" fill="none" stroke="#ffffff" stroke-width="2"/></svg>Reliable and friendly service</li>
        <li><svg width="11" height="10" viewBox="0 0 11 10"><path d="M1 5l3 3 6-7" fill="none" stroke="#ffffff" stroke-width="2"/></svg>12 years experience</li>
        <li><svg width="11" height="10" viewBox="0 0 11 10"><path d="M1 5l3 3 6-7" fill="none" stroke="#ffffff" stroke-width="2"/></svg>Great rates</li>
      </ul>
    </header>

    <div class="tagline-band">
      <h1 class="tagline">A beautiful garden doesn't happen by itself</h1>
    </div>

    <p class="intro">Marlowe Greens is your garden and lawn care specialist, with a passion for gardening and a keen eye for detail you can rest assured you're in the right hands.</p>

    <h2 class="services-title">Our Services</h2>
    <div class="services">
      <ul>
        <li>- pressure cleaning,</li>
        <li>- Eco Friendly fertilizing,</li>
        <li>- green waste removal,</li>
        <li>- tree and shrub pruning,</li>
        <li>- Full garden makeovers,</li>
        <li>- Timber deck rejuvenation,</li>
        <li>- Turf preparation and installation,</li>
      </ul>
      <ul>
        <li>- lawn mowing,</li>
        <li>- weeding,</li>
        <li>- Mulching,</li>
        <li>- hedging,</li>
        <li>- privacy screening,</li>
        <li>- Planting,</li>
        <li>- and much more</li>
      </ul>
    </div>

    <h2 class="cta">Book an appointment</h2>

    <footer class="contact-band">
      <p>Phone 0418527064<span class="divider">|</span>www.marlowegreens.com.au</p>
      <p>Email doug@marlowegreens.com.au</p>
    </footer>
  </article>
</body>
</html>
```